Banner Ad Design Project

I just launched an affiliate program for my company (Brisk Academy), and I need some web ads and banners created. 6 in total.Here are the specs for the ads:
W120XH90- Small Web Ad
W120XH160- Big Web Ad
W468XH60- Full Banner Ad
W250XH250- Big Banner Ad
W125XH125- Samll Square Ad
W160XH600- Wide Skyscraper
I've uploaded one example I made hower I am looking for a more professional look. You'll also see a few flyers I've uploaded. These will get you an idea of the product.
Here is what I am looking to achieve and a little background on my product:
BRISK Academy’s first course, ‘Ready on Shift’ is a 30 minute interactive training and certification course specifically designed for teens and young adults to better prepare them for the workplace. The training is based on employer feedback, delivered on a peer-to-peer level, industry nonspecific, mobile ready and covers the following challenges:
• Work Ethic
• Social Media
• Cell Phone Issues
• Communication and Manners Matter
• Hygiene and more.
These ads are to catch the eyes of bosses, supervisors and managers. Basically anyone who is looking to improve workplace performance. Our website is www.briskacademy.example. Please look it over for our branding. Thanks so much!
ps- Please make 1/2 static banners and 1/2 animated (gif of flash) banner.
Target Market(s)
Bosses, supervisors and managers. Anyone who employees teenagers and young adults and is looking to train them to better serve their customers.
Industry/Entity Type
Training
Look and feel

```html
<!DOCTYPE html>
<html lang="en">
<head>
<meta charset="utf-8">
<title>Brisk Academy – Banner Set</title>
<link rel="stylesheet" href="https://fonts.googleapis.com/css2?family=Cabin+Sketch:wght@400;700&family=Patrick+Hand&family=Open+Sans:wght@400;700&display=swap">
<style>
  :root {
    --canvas-grey: #b1b1b1;
    --board-dark: #2b2b2b;
    --board-mid: #4a4a4a;
    --chalk: #f2f2f2;
    --chalk-green: #b8e07a;
    --paper: #ffffff;
    --paper-shade: #dcdcdc;
    --brand-red: #e0283a;
    --brand-blue: #1d3f9a;
    --note-yellow: #fbf95a;
    --note-ink: #3a3a3a;
    --note-accent: #ff4a14;
    --apple-red: #c7161d;
    --apple-dark: #6e0a0e;
  }
  * { margin: 0; padding: 0; box-sizing: border-box; }
  html, body { width: 1200px; height: 900px; overflow: hidden; }
  body { background: var(--canvas-grey); position: relative; font-family: "Open Sans", Arial, sans-serif; }

  .banner {
    position: absolute; top: 271px; width: 372px; height: 372px; overflow: hidden;
    background: radial-gradient(ellipse at 40% 35%, var(--board-mid), var(--board-dark) 80%);
  }
  .banner--headline { left: 196px; }
  .banner--offer { left: 612px; }

  .headline { position: absolute; left: 24px; top: 16px; font-family: "Cabin Sketch", cursive; color: var(--chalk); line-height: 1; font-weight: 400; }
  .headline__top { display: block; font-size: 42px; letter-spacing: 2px; }
  .headline__main { display: block; font-size: 64px; letter-spacing: 2px; margin-top: 2px; }

  .tagline { position: absolute; left: 26px; top: 144px; width: 205px; color: var(--chalk); font-size: 16px; line-height: 35px; white-space: nowrap; }

  .grade-mark {
    position: absolute; left: 254px; top: 116px; width: 50px; height: 50px; border-radius: 50%;
    border: 2px solid var(--chalk-green); color: var(--chalk-green);
    font-family: "Cabin Sketch", cursive; font-weight: 700; font-size: 26px;
    display: flex; align-items: center; justify-content: center; opacity: .85;
  }

  .paper-strip {
    position: absolute; left: 0; bottom: 0; width: 100%; height: 122px;
    background: linear-gradient(180deg, var(--paper) 0%, var(--paper) 55%, var(--paper-shade) 100%);
    clip-path: polygon(0 14%, 8% 10%, 16% 16%, 26% 8%, 35% 14%, 46% 6%, 57% 12%, 66% 5%, 76% 11%, 88% 4%, 100% 9%, 100% 100%, 0 100%);
  }

  .apple {
    position: absolute; left: 240px; top: 178px; width: 140px; height: 122px; border-radius: 50% 50% 46% 46% / 52% 52% 48% 48%;
    background: radial-gradient(ellipse at 35% 35%, #f0464a, var(--apple-red) 50%, var(--apple-dark) 100%);
  }
  .apple-reflection {
    position: absolute; left: 244px; top: 298px; width: 134px; height: 60px; border-radius: 50%;
    background: radial-gradient(ellipse at 50% 20%, rgba(199,22,29,.22), rgba(199,22,29,0) 70%);
  }

  .brand { position: absolute; left: 20px; bottom: 18px; display: flex; align-items: center; gap: 10px; }
  .brand__dot { width: 34px; height: 34px; border-radius: 50%; background: var(--brand-blue); }
  .brand__name { color: var(--brand-red); font-weight: 700; font-size: 27px; }

  .sticky-note { position: absolute; left: 0; top: 0; width: 300px; height: 250px; }
  .sticky-note__text {
    position: absolute; left: 30px; top: 14px; font-family: "Patrick Hand", cursive;
    color: var(--note-ink); font-size: 38px; line-height: 43px;
  }
  .sticky-note__text .accent { color: var(--note-accent); }
  .banner--offer .grade-mark { z-index: 2; }
</style>
</head>
<body>

  <section class="banner banner--headline">
    <h1 class="headline">
      <span class="headline__top">READY ON</span>
      <span class="headline__main">SHIFT</span>
    </h1>
    <p class="tagline">Web based training for<br>Teens and Young Adults</p>
    <div class="grade-mark">A+</div>
    <div class="paper-strip"></div>
    <div class="apple-reflection"></div>
    <div class="apple" role="img" aria-label="Red apple with green leaf"></div>
    <div class="brand">
      <span class="brand__dot"></span>
      <span class="brand__name">Brisk Academy</span>
    </div>
  </section>

  <section class="banner banner--offer">
    <div class="paper-strip"></div>
    <div class="apple-reflection"></div>
    <div class="apple" role="img" aria-label="Red apple with green leaf"></div>
    <div class="brand">
      <span class="brand__dot"></span>
      <span class="brand__name">Brisk Academy</span>
    </div>
    <svg class="sticky-note" viewBox="0 0 300 250" aria-hidden="true">
      <path d="M0 0 H282 Q278 120 296 232 Q200 222 20 236 L0 236 Z" fill="#1a1a1a"/>
      <path d="M0 0 H276 Q270 120 290 226 Q200 216 18 232 L0 232 Z" fill="var(--note-yellow)"/>
    </svg>
    <p class="sticky-note__text">Visit website<br>for a <span class="accent">FREE</span><br>sneak Peek!</p>
    <div class="grade-mark">A+</div>
  </section>

</body>
</html>
```